Innovative Consulting Firm Needs New Business Cards and Stationary

Our Innovative Consulting Firm, Larkfield Consulting, is in need of new business cards and stationary designs. We want two-sided cards that incorporate our logo, which is attached. We are looking for something not too formal, but is professional and slick.

Card should have the following information:
Name (ex. Tom Bradley)
Title (ex. Manager)
Address (ex. 24680 Cedar Lane)
Address 2 (ex. Suite 100)
City
State
Zip Code
Mobile
Email

The card should also have our website: www.larkfieldconsulting.example

Industry/Entity Type

Management Consulting

Contact Information for Business Card

Name (ex. Tom Bradley)
Title (ex. Manager)
Address 2 (ex. Suite 100)
City
State
Zip Code
Mobile
Email

Font styles to use
Sans Serif

Requirements
Must have
• The colors on the card must match the colors in the logo. The exact color codes are attached in a pdf.
Nice to have
• The Company's Tagline is "Focused on your Future". This might be nice to incorporate, but not necessary.

```html
<!DOCTYPE html>
<html lang="en">
<head>
<meta charset="utf-8">
<title>Larkfield Consulting — Business Card</title>
<link href="https://fonts.googleapis.com/css2?family=Open+Sans:wght@300;400;600&display=swap" rel="stylesheet">
<style>
  :root {
    --page: #ecebe8;
    --card-white: #ffffff;
    --brand-blue: #1f5a97;
    --brand-blue-light: #3478bd;
    --brand-blue-dark: #174679;
    --brand-yellow: #f2c12e;
    --ink: #4a4f57;
    --ink-soft: #8a9099;
  }
  * { box-sizing: border-box; margin: 0; padding: 0; }
  html, body { width: 783px; height: 1200px; overflow: hidden; }
  body {
    background: var(--page);
    font-family: "Open Sans", Arial, sans-serif;
    color: var(--ink);
    display: flex;
    flex-direction: column;
    align-items: center;
    justify-content: center;
    gap: 90px;
  }
  .card {
    position: relative;
    width: 620px;
    height: 354px;
    border-radius: 6px;
    overflow: hidden;
    box-shadow: 0 4px 14px rgba(0,0,0,.12);
  }

  /* ---------- Contact side ---------- */
  .card--contact { background: var(--card-white); }
  .card--contact .swoosh { position: absolute; inset: 0; }
  .card--contact .wordmark {
    position: absolute;
    left: 40px;
    top: 150px;
    display: flex;
    align-items: center;
    gap: 10px;
    color: var(--brand-blue);
    font-weight: 400;
    font-size: 27px;
    letter-spacing: .5px;
  }
  .wordmark .mark-square {
    width: 16px; height: 16px;
    background: var(--brand-yellow);
  }
  .person {
    position: absolute;
    right: 74px;
    top: 40px;
    text-align: right;
  }
  .person__name { font-size: 22px; font-weight: 400; color: var(--ink); }
  .person__title { font-size: 13px; color: var(--ink-soft); margin-top: 2px; }
  .name-tab {
    position: absolute;
    right: 30px; top: 40px;
    width: 30px; height: 46px;
    background: var(--brand-blue);
  }
  .contact-list {
    position: absolute;
    right: 40px;
    top: 170px;
    list-style: none;
    font-size: 12.5px;
    line-height: 1;
  }
  .contact-list li {
    display: flex;
    align-items: center;
    gap: 10px;
    margin-bottom: 12px;
  }
  .contact-list svg { width: 13px; height: 13px; fill: var(--brand-blue); flex: none; }
  .contact-list .indent { padding-left: 23px; }

  /* ---------- Brand side ---------- */
  .card--brand {
    background: linear-gradient(135deg, var(--brand-blue-light) 0%, var(--brand-blue) 55%, var(--brand-blue-dark) 100%);
    display: flex;
    align-items: center;
    justify-content: center;
  }
  .card--brand .wordmark {
    display: flex;
    align-items: center;
    gap: 14px;
    color: #ffffff;
    font-weight: 400;
    font-size: 40px;
    letter-spacing: .5px;
  }
  .card--brand .mark-square { width: 22px; height: 22px; }
</style>
</head>
<body>

  <section class="card card--contact" aria-label="Business card, contact side">
    <svg class="swoosh" viewBox="0 0 620 354" aria-hidden="true">
      <path d="M0 262 C170 250 300 190 388 0" fill="none" stroke="var(--brand-yellow)" stroke-width="7"/>
      <path d="M0 282 C190 270 330 200 420 0" fill="none" stroke="var(--brand-yellow)" stroke-width="2" opacity=".7"/>
      <path d="M220 354 C240 300 280 270 330 262 L330 354 Z" fill="var(--brand-yellow)" opacity=".9"/>
    </svg>

    <div class="wordmark"><span class="mark-square"></span>Larkfield Consulting</div>

    <div class="person">
      <p class="person__name">Tom Bradley</p>
      <p class="person__title">Manager</p>
    </div>
    <div class="name-tab"></div>

    <ul class="contact-list">
      <li><svg viewBox="0 0 24 24"><path d="M12 2a7 7 0 0 0-7 7c0 5 7 13 7 13s7-8 7-13a7 7 0 0 0-7-7zm0 9.5A2.5 2.5 0 1 1 12 6.5a2.5 2.5 0 0 1 0 5z"/></svg>24680 Cedar Lane, Suite 100</li>
      <li class="indent">Northvale, OH 45000</li>
      <li><svg viewBox="0 0 24 24"><path d="M6.6 10.8a15 15 0 0 0 6.6 6.6l2.2-2.2a1 1 0 0 1 1-.25 11.4 11.4 0 0 0 3.6.57 1 1 0 0 1 1 1V20a1 1 0 0 1-1 1A17 17 0 0 1 3 4a1 1 0 0 1 1-1h3.5a1 1 0 0 1 1 1c0 1.25.2 2.45.57 3.57a1 1 0 0 1-.25 1z"/></svg>555-010-2400</li>
      <li><svg viewBox="0 0 24 24"><path d="M3 5h18v14H3zm2 2v.5l7 4.5 7-4.5V7z"/></svg>tom@larkfieldconsulting.example</li>
      <li><svg viewBox="0 0 24 24"><circle cx="12" cy="12" r="9" fill="none" stroke="var(--brand-blue)" stroke-width="2"/><path d="M3 12h18M12 3c3 3 3 15 0 18M12 3c-3 3-3 15 0 18" fill="none" stroke="var(--brand-blue)" stroke-width="1.6"/></svg>www.larkfieldconsulting.example</li>
    </ul>
  </section>

  <section class="card card--brand" aria-label="Business card, brand side">
    <div class="wordmark"><span class="mark-square"></span>Larkfield Consulting</div>
  </section>

</body>
</html>
```